Web Design Project - Vextrion

We have created an initial website at http://www.vextrion-example.com

This project requires you to take the current website and redesigning it to improve the overall look and feel.

Feel free to experiment with everything including:

~ colour schemes
~ layout

The only constraints are

- the text content
- the app icons on /games
- the logo structure (feel free to change the colour schemes / logo image)

In terms of process - please feel free to post concepts / mockups for one page - if this is easier for you to do quickly (without revamping the entire site).

As well as the website, please provide designs for a facebook page cover and profile picture for http://www.socialpage-example.com/pages/Vextrion/730194652018364

Thanks for the submissions - but we've not quite found what we're looking for.

This site is on which appeals to us - please use this for inspiration: http://brambury-example.com/

Thanks

Reason: I am about to make this project "guaranteed" and want to give more time to submit

Please submit your creative ideas - we look forward to receiving them.

Reason: Hi, Deadline extended so that we can see revisions Thanks

Target Market(s)

Marketing Executives / CEOs of Media Companies

Industry/Entity Type

Games

```html
<!DOCTYPE html>
<html lang="en">
<head>
<meta charset="utf-8">
<title>Vextrion – In-play second screen games</title>
<link rel="stylesheet" href="https://fonts.googleapis.com/css2?family=Kalam:wght@400&family=Arimo:ital,wght@0,400;0,700;1,400;1,700&display=swap">
<style>
  :root {
    --page-bg: #fbfcfd;
    --top-rule: #8c8c8c;
    --navy: #1b3d73;
    --teal: #2ba3b8;
    --teal-light: #bfe3e8;
    --hero-top: #d6eaf8;
    --hero-bottom: #ffffff;
    --ink: #1c1c1c;
    --body-ink: #3b3b3b;
    --heading-blue: #1e3f72;
    --accent-red: #c8161d;
    --panel-bg: #e9eef3;
    --panel-border: #cfd6dd;
    --link-teal: #2598b0;
    --white: #ffffff;
  }
  * { box-sizing: border-box; margin: 0; padding: 0; }
  html, body { width: 1200px; height: 1133px; overflow: hidden; }
  body {
    position: relative;
    background: var(--page-bg);
    font-family: "Arimo", Arial, sans-serif;
    color: var(--ink);
    border-top: 4px solid var(--top-rule);
  }

  /* Header */
  .brand {
    position: absolute; left: 252px; top: 30px; width: 150px; height: 100px;
    display: flex; align-items: center; gap: 10px;
  }
  .brand-mark { width: 22px; height: 22px; background: var(--accent-red); flex: none; }
  .brand-name { font-family: "Kalam", cursive; font-size: 30px; color: var(--navy); }

  .social-links { position: absolute; left: 877px; top: 9px; display: flex; gap: 3px; list-style: none; }
  .social-links li { width: 22px; height: 22px; background: #2f63b3; border-radius: 3px; }
  .social-links li:last-child { background: #222; }

  .main-nav {
    position: absolute; left: 442px; top: 72px; width: 559px; height: 50px;
    border: 1px solid #c7c7c7; border-radius: 5px;
    background: linear-gradient(#ffffff, #e6e6e6);
    box-shadow: 0 2px 3px rgba(0,0,0,.18);
    display: flex; padding-left: 54px; list-style: none;
  }
  .main-nav li {
    font-size: 13px; font-weight: 700; color: var(--ink);
    padding: 0 15px; line-height: 48px;
  }
  .main-nav li.is-active { background: linear-gradient(#d9eef1, var(--teal-light)); }

  /* Tagline band */
  .tagline {
    position: absolute; left: 0; top: 146px; width: 1200px; height: 55px;
    background: var(--teal);
    color: var(--white); font-size: 22px; text-align: center; line-height: 55px;
  }

  /* Hero */
  .hero {
    position: absolute; left: 0; top: 201px; width: 1200px; height: 403px;
    background: linear-gradient(var(--hero-top), var(--hero-bottom));
  }
  .hero::after {
    content: ""; position: absolute; left: 210px; right: 200px; bottom: -34px; height: 34px;
    background: radial-gradient(ellipse at top, rgba(0,0,0,.12), transparent 70%);
  }
  .hero-divider {
    position: absolute; left: 599px; top: 30px; width: 2px; height: 360px;
    background: linear-gradient(rgba(255,255,255,0), rgba(180,200,215,.7), rgba(255,255,255,0));
  }
  .hero-copy {
    position: absolute; top: 26px; width: 380px;
    font-family: "Kalam", cursive; font-size: 19px; line-height: 25px;
    color: var(--heading-blue); text-align: center;
  }
  .hero-copy--games { left: 200px; }
  .hero-copy--screens { left: 605px; color: #222; }
  .hero-copy .highlight { color: var(--accent-red); }
  .hero-art { position: absolute; }
  .hero-art--games {
    left: 239px; top: 107px; width: 277px; height: 277px;
    background: radial-gradient(closest-side, #3cb6d4 0%, #2378a8 45%, rgba(27,74,128,.55) 75%, rgba(27,74,128,0) 100%);
  }
  .hero-art--screens {
    left: 627px; top: 120px; width: 336px; height: 240px;
    background: radial-gradient(closest-side, #7a7a7a 0%, #4a4a4a 50%, rgba(51,51,51,.5) 78%, rgba(51,51,51,0) 100%);
  }

  /* Audience panels */
  .audience { position: absolute; top: 651px; width: 387px; }
  .audience--owners { left: 205px; }
  .audience--players { left: 607px; }
  .audience-title {
    position: relative; height: 58px;
    border: 1px solid var(--panel-border); border-radius: 4px;
    background: linear-gradient(#ffffff, #f1f3f5);
    font-size: 15px; font-weight: 400; color: #333; text-align: center;
    display: flex; align-items: center; justify-content: center; padding: 0 22px; line-height: 19px;
  }
  .audience-title::after {
    content: ""; position: absolute; left: 50%; bottom: -9px; margin-left: -9px;
    border-left: 9px solid transparent; border-right: 9px solid transparent; border-top: 9px solid #d4d9de;
  }
  .audience-body {
    position: relative; margin-top: 28px; height: 251px;
    border: 1px solid var(--panel-border); border-radius: 5px;
    background: linear-gradient(#f4f6f9, var(--panel-bg));
    padding: 18px 18px 0 32px;
  }
  .audience-list { list-style: none; }
  .audience-list li {
    position: relative; font-size: 11.5px; line-height: 20.5px; color: var(--body-ink);
    text-align: justify;
  }
  .audience-list li::before {
    content: ""; position: absolute; left: -16px; top: 7px;
    width: 5px; height: 5px; border-top: 1.5px solid #5b7ea8; border-right: 1.5px solid #5b7ea8;
    transform: rotate(45deg);
  }
  .read-more {
    position: absolute; right: -1px; bottom: -1px; width: 115px; height: 28px;
    background: var(--page-bg); border-top-left-radius: 10px;
    font-style: italic; font-weight: 700; font-size: 12px; color: var(--link-teal);
    text-align: center; line-height: 30px;
  }

  /* Footer */
  .footer-nav {
    position: absolute; left: 0; top: 1022px; width: 1200px; height: 61px;
    background: var(--navy);
    display: flex; justify-content: center; align-items: center; gap: 14px;
    list-style: none; font-size: 13px; color: var(--white);
  }
  .footer-nav li + li::before { content: "/"; margin-right: 14px; }
  .footer-nav li.is-active { color: #4fb8d8; }
  .legal {
    position: absolute; left: 0; top: 1083px; width: 1200px; height: 50px;
    background: var(--teal); color: var(--white);
    font-size: 11.5px; text-align: center; line-height: 18px; padding-top: 7px;
  }
</style>
</head>
<body>
  <header>
    <div class="brand"><span class="brand-mark"></span><span class="brand-name">Vextrion</span></div>
    <ul class="social-links" aria-label="Social links"><li></li><li></li><li></li><li></li><li></li></ul>
    <ul class="main-nav">
      <li class="is-active">Home</li><li>About</li><li>Games</li><li>Solutions</li><li>Updates</li><li>Contact</li>
    </ul>
  </header>

  <div class="tagline">"Delivering in-play second screen games based on live broadcast events"</div>

  <section class="hero">
    <p class="hero-copy hero-copy--games"><span class="highlight">In-Play Games</span> allow players to interact with real-time scoring whilst watching live events with instant scoring.</p>
    <p class="hero-copy hero-copy--screens">Second-Screens are mobile phones or tablets used by viewers to enrich their TV watching experience.</p>
    <div class="hero-art hero-art--games" role="img" aria-label="Cartoon TV mascot holding a microphone and bat, standing on a football"></div>
    <div class="hero-divider"></div>
    <div class="hero-art hero-art--screens" role="img" aria-label="Grey TV mascot holding a phone and tablet, labelled with mobile platforms, standing on a football"></div>
  </section>

  <section class="audience audience--owners">
    <h2 class="audience-title">For Media Owners, Broadcasters or Sponsors of Live Events</h2>
    <div class="audience-body">
      <ul class="audience-list">
        <li>Games can be re-skinned &amp; launched for your live event</li>
        <li>Increases value of live media rights through increased viewer engagement</li>
        <li>Games capture extensive customer data to enhance your CRM capabilities</li>
        <li>Deep social network integration and social gameplay mechanisms maximise chances of the game "going viral"</li>
        <li>Click here to find out more about our Solutions</li>
      </ul>
      <span class="read-more">Read more</span>
    </div>
  </section>

  <section class="audience audience--players">
    <h2 class="audience-title">For Game Players and Fans</h2>
    <div class="audience-body">
      <ul class="audience-list">
        <li>Play games with friends while watching live events</li>
        <li>Real-time gameplay based on the event you're watching</li>
        <li>Compete against your friends and other players</li>
        <li>Free to play prizes for the best performing games</li>
        <li>Click here to see a list of our games</li>
      </ul>
      <span class="read-more">Read more</span>
    </div>
  </section>

  <footer>
    <ul class="footer-nav">
      <li class="is-active">Home</li><li>About</li><li>Games</li><li>Solutions</li><li>Updates</li><li>Contact</li>
    </ul>
    <div class="legal">
      Use of this Web site constitutes acceptance of Vextrion's Terms of Service and Privacy Policy<br>
      © Copyright 2012 Halvenor Systems Ltd. All rights reserved.
    </div>
  </footer>
</body>
</html>
```